International school needs an amazing design for our character traits!

We are the Corvell School of Demarre and promote character traits using an acronym of our school mascot, the FALCONS.
Fearless
Aware
Leaders
Curious
Open-minded
Noble
Self-motivated

Right now, these are only words on a page that we try to bring to life. It would be great to have a visual to go with the words - to promote the image of what we are looking for.

Target Market(s)

Students and Families

Industry/Entity Type

Education

Font styles to use
Sans Serif

Colors

Designer to choose colors to be used in the design.

Requirements
Must have
• Images

```html
<!DOCTYPE html>
<html lang="en">
<head>
<meta charset="utf-8">
<title>FALCONS Character Traits – Corvell School of Demarre</title>
<link rel="stylesheet" href="https://fonts.googleapis.com/css2?family=Lato:ital,wght@0,400;0,700;0,900;1,700&family=Oswald:wght@600&display=swap">
<style>
  :root {
    --backdrop: #333333;
    --paper: #f7f7f7;
    --blue: #1a4f9c;
    --red: #e23b3b;
    --white: #ffffff;
    --ink: #222222;
    --icon-blue: #c9d6ea;
    --icon-red: #f4c9c9;
  }
  * { box-sizing: border-box; margin: 0; padding: 0; }
  html, body { width: 1200px; height: 1177px; overflow: hidden; }
  body {
    background: var(--backdrop);
    font-family: "Lato", Arial, sans-serif;
    position: relative;
  }
  .poster {
    position: absolute;
    left: 274px; top: 112px;
    width: 680px; height: 962px;
    background: linear-gradient(180deg, #ffffff 0%, var(--paper) 45%, #ececec 100%);
    overflow: hidden;
  }
  .top-band {
    position: absolute; left: 0; top: 0; width: 100%; height: 78px;
    background: linear-gradient(90deg, var(--blue) 0%, var(--blue) 25%, #7d4470 60%, var(--red) 85%);
  }
  .bottom-band {
    position: absolute; left: 0; bottom: 0; width: 100%; height: 40px;
    background: var(--blue);
  }
  .school-seal {
    position: absolute; left: 470px; top: 2px;
    width: 188px; height: 188px; border-radius: 50%;
    background: var(--white);
    box-shadow: 0 4px 12px rgba(0,0,0,.25);
    display: flex; align-items: center; justify-content: center;
    text-align: center;
  }
  .school-name {
    color: var(--blue); font-weight: 900; font-size: 19px;
    line-height: 1.15; text-transform: uppercase; width: 140px;
  }
  .mascot-photo {
    position: absolute; left: 340px; top: 330px;
    width: 340px; height: 600px;
    background: radial-gradient(ellipse closest-side at 60% 50%, #c4c4c4 0%, #d8d8d8 45%, rgba(236,236,236,0) 100%);
    opacity: .85;
  }
  .traits { position: absolute; left: 44px; top: 150px; list-style: none; }
  .trait {
    position: absolute; left: 0;
    width: 400px; height: 76px;
    border-radius: 38px;
    background: #f2f2f2;
    box-shadow: 0 2px 8px rgba(0,0,0,.12);
  }
  .trait-icon {
    position: absolute; left: 4px; top: 4px;
    width: 118px; height: 68px; border-radius: 34px;
    background: var(--white);
  }
  .icon-art {
    position: absolute; left: 30px; top: 15px;
    width: 38px; height: 38px; border-radius: 50%;
    background: linear-gradient(135deg, var(--icon-blue) 0%, var(--icon-red) 100%);
  }
  .trait-bar {
    position: absolute; left: 126px; top: 5px;
    width: 264px; height: 66px; border-radius: 0 33px 33px 0;
    display: flex; align-items: center; padding-left: 58px;
    color: var(--white); font-weight: 700; font-size: 19px; line-height: 1.1;
    text-transform: uppercase;
  }
  .trait-letter {
    position: absolute; left: 92px; top: 4px;
    width: 68px; height: 68px; border-radius: 50%;
    border: 4px solid var(--white);
    display: flex; align-items: center; justify-content: center;
    color: var(--white); font-family: "Oswald", "Lato", sans-serif;
    font-weight: 600; font-size: 34px; line-height: 1;
  }
  .is-red-letter .trait-letter { background: var(--red); }
  .is-red-letter .trait-bar { background: var(--blue); }
  .is-blue-letter .trait-letter { background: var(--blue); }
  .is-blue-letter .trait-bar { background: var(--red); }
  .credit {
    position: absolute; right: 30px; bottom: 50px;
    font-size: 10px; font-weight: 700; font-style: italic; color: var(--ink);
  }
</style>
</head>
<body>
  <main class="poster">
    <div class="top-band"></div>
    <div class="school-seal"><span class="school-name">Corvell School of Demarre</span></div>

    <div class="mascot-photo" role="img" aria-label="Photograph of a falcon perched and looking left, faded in grey"></div>

    <ul class="traits">
      <li class="trait is-red-letter" style="top:-4px">
        <span class="trait-icon"><span class="icon-art" role="img" aria-label="Icon for fearless"></span></span>
        <span class="trait-bar">Fearless</span>
        <span class="trait-letter">F</span>
      </li>
      <li class="trait is-blue-letter" style="top:108px">
        <span class="trait-icon"><span class="icon-art" role="img" aria-label="Icon for aware"></span></span>
        <span class="trait-bar">Aware</span>
        <span class="trait-letter">A</span>
      </li>
      <li class="trait is-red-letter" style="top:218px">
        <span class="trait-icon"><span class="icon-art" role="img" aria-label="Icon for leaders"></span></span>
        <span class="trait-bar">Leaders</span>
        <span class="trait-letter">L</span>
      </li>
      <li class="trait is-blue-letter" style="top:325px">
        <span class="trait-icon"><span class="icon-art" role="img" aria-label="Icon for curious"></span></span>
        <span class="trait-bar">Curious</span>
        <span class="trait-letter">C</span>
      </li>
      <li class="trait is-red-letter" style="top:434px">
        <span class="trait-icon"><span class="icon-art" role="img" aria-label="Icon for open-minded"></span></span>
        <span class="trait-bar">Open-minded</span>
        <span class="trait-letter">O</span>
      </li>
      <li class="trait is-blue-letter" style="top:547px">
        <span class="trait-icon"><span class="icon-art" role="img" aria-label="Icon for noble"></span></span>
        <span class="trait-bar">Noble</span>
        <span class="trait-letter">N</span>
      </li>
      <li class="trait is-red-letter" style="top:655px">
        <span class="trait-icon"><span class="icon-art" role="img" aria-label="Icon for self-motivated"></span></span>
        <span class="trait-bar">Self-<br>motivated</span>
        <span class="trait-letter">S</span>
      </li>
    </ul>

    <p class="credit">Icons by Pixelnest from Iconwell.com</p>
    <div class="bottom-band"></div>
  </main>
</body>
</html>
```